Business Cards

Business card design for my company.
I would like the card's background colour to be black. You can also see our web site to get an idea of our brand. https://www.dlqmarrowfield.com.au/
- Name
- Email

```html
<!DOCTYPE html>
<html lang="en">
<head>
<meta charset="utf-8">
<title>DLQ Marrowfield – Business Cards</title>
<link href="https://fonts.googleapis.com/css2?family=Poppins:wght@400;500;700&display=swap" rel="stylesheet">
<style>
  :root {
    --stage: #d6d6d6;
    --card-black: #050505;
    --brand-green: #1a9a4a;
    --paper-white: #ffffff;
    --ink: #111111;
    --soft-white: #f2f2f2;
  }
  * { box-sizing: border-box; margin: 0; padding: 0; }
  html, body { width: 1200px; height: 961px; overflow: hidden; }
  body {
    background: var(--stage);
    font-family: "Poppins", sans-serif;
    position: relative;
  }
  .card {
    position: absolute;
    width: 540px;
    height: 309px;
    background: var(--card-black);
    overflow: hidden;
    box-shadow: 0 10px 24px rgba(0,0,0,0.25);
  }
  .card--back { left: 40px; top: 470px; }
  .card--front { left: 620px; top: 180px; }

  /* Back: brand name and website */
  .brand-block {
    position: absolute;
    left: 0; right: 0; top: 92px;
    display: flex; flex-direction: column; align-items: center; gap: 22px;
  }
  .brand-name {
    display: flex; align-items: center; gap: 12px;
    color: var(--soft-white);
    font-weight: 700;
    font-size: 34px;
    letter-spacing: 3px;
  }
  .brand-mark-square {
    width: 18px; height: 18px; background: var(--brand-green);
  }
  .website {
    font-size: 15px; font-weight: 400; letter-spacing: 2.5px; color: var(--soft-white);
  }
  .website .domain { color: var(--brand-green); }

  /* Front */
  .front-brand {
    position: absolute; left: 26px; top: 30px;
    display: flex; align-items: center; gap: 9px;
    color: var(--soft-white); font-weight: 700; font-size: 20px; letter-spacing: 2px;
  }
  .front-brand .brand-mark-square { width: 12px; height: 12px; }
  .name-tag {
    position: absolute; right: 0; top: 92px;
    width: 210px; height: 56px;
    background: var(--brand-green);
    clip-path: polygon(14% 0, 100% 0, 100% 100%, 0 100%, 0 30%);
    color: var(--paper-white);
    padding: 8px 16px 0 44px;
    text-align: right;
  }
  .name-tag .person-name { font-weight: 700; font-size: 17px; letter-spacing: 1px; line-height: 1.2; }
  .name-tag .person-role { font-weight: 400; font-size: 10.5px; letter-spacing: 1.2px; }
  .name-underline {
    position: absolute; right: 0; top: 152px; width: 200px; height: 5px; background: var(--paper-white);
  }
  .photo-strip { position: absolute; left: 0; top: 165px; width: 540px; height: 86px; }
  .contact-band {
    position: absolute; left: 0; bottom: 0; width: 540px; height: 58px;
    background: var(--paper-white);
    display: flex; align-items: center; justify-content: center; gap: 18px;
    color: var(--ink); font-size: 13px; letter-spacing: 0.5px;
  }
  .contact-item { display: flex; align-items: center; gap: 7px; }
  .contact-icon { width: 16px; height: 16px; }
  .contact-divider { color: var(--ink); font-size: 15px; }
</style>
</head>
<body>

<section class="card card--back" aria-label="Business card back">
  <div class="brand-block">
    <div class="brand-name"><span class="brand-mark-square"></span>DLQ MARROWFIELD</div>
    <div class="website">www.<span class="domain">dlqmarrowfield</span>.com.au</div>
  </div>
</section>

<section class="card card--front" aria-label="Business card front">
  <div class="front-brand"><span class="brand-mark-square"></span>DLQ MARROWFIELD</div>

  <div class="name-tag">
    <div class="person-name">LIAM HARTLEY</div>
    <div class="person-role">GENERAL MANAGER</div>
  </div>
  <div class="name-underline"></div>

  <svg class="photo-strip" viewBox="0 0 540 86" aria-hidden="false">
    <defs>
      <linearGradient id="photoLiving" x1="0" y1="0" x2="1" y2="1">
        <stop offset="0" stop-color="#b27a45"/><stop offset="1" stop-color="#9fb3c6"/>
      </linearGradient>
      <linearGradient id="photoBathroom" x1="0" y1="0" x2="1" y2="1">
        <stop offset="0" stop-color="#f1f1ef"/><stop offset="1" stop-color="#8d8a86"/>
      </linearGradient>
      <linearGradient id="photoKitchen" x1="0" y1="0" x2="1" y2="1">
        <stop offset="0" stop-color="#d49a5e"/><stop offset="1" stop-color="#efe3d4"/>
      </linearGradient>
      <linearGradient id="photoFacade" x1="0" y1="0" x2="1" y2="1">
        <stop offset="0" stop-color="#7a4a28"/><stop offset="1" stop-color="#b9bcc0"/>
      </linearGradient>
    </defs>
    <rect x="0" y="0" width="540" height="86" fill="#1a9a4a"/>
    <g role="img" aria-label="Photo of a timber-lined living room with a valley view">
      <polygon points="4,4 140,4 120,82 4,82" fill="url(#photoLiving)"/>
    </g>
    <g role="img" aria-label="Photo of a bright white bathroom with a glass shower">
      <polygon points="146,4 270,4 250,82 126,82" fill="url(#photoBathroom)"/>
    </g>
    <g role="img" aria-label="Photo of a warm timber kitchen with pendant lights">
      <polygon points="276,4 400,4 380,82 256,82" fill="url(#photoKitchen)"/>
    </g>
    <g role="img" aria-label="Photo of a timber-battened house facade with large windows">
      <polygon points="406,4 536,4 536,82 386,82" fill="url(#photoFacade)"/>
    </g>
  </svg>

  <div class="contact-band">
    <div class="contact-item">
      <svg class="contact-icon" viewBox="0 0 16 16" aria-hidden="true">
        <circle cx="8" cy="8" r="8" fill="#1a9a4a"/>
        <path d="M5.2 4.2l1.4-.3.8 1.8-.9.7c.4.9 1.1 1.6 2 2l.7-.9 1.8.8-.3 1.4c-3 .2-5.7-2.5-5.5-5.5z" fill="#fff"/>
      </svg>
      <span>0400 123 456</span>
    </div>
    <span class="contact-divider">/</span>
    <div class="contact-item">
      <svg class="contact-icon" viewBox="0 0 16 16" aria-hidden="true">
        <circle cx="8" cy="8" r="8" fill="#1a9a4a"/>
        <rect x="4" y="5" width="8" height="6" fill="#fff"/>
        <path d="M4 5l4 3.2L12 5" stroke="#1a9a4a" stroke-width="0.9" fill="none"/>
      </svg>
      <span>info@dlqmarrowfield.com.au</span>
    </div>
  </div>
</section>

</body>
</html>
```